Corporate Design für Vermittlung von wertigen Immobilien
Zielgruppe
Vermittlung von wertigen Immobilien.
Zielgruppe sind Verkäufer von hochwertigen Gebäuden und Käufer, die ordentliche (wertige) Immobilien suchen.
Eventuell auch im Bereich Vermietung. Mein Fokus wird eher auf den Kaufobjekten liegen.
Aufgabenstellung
Liebe Designer, für meinen neuen Geschäftszweig (Makler) benötige ich Visitenkarten und Briefpapier. Des weiteren möchte ich gerne eine Präsentationsmappe , in der ich den Kunden Informationen zum Objekt (Exposé) und die Vertragsunterlagen (Maklervertrag) im Format DINA4 übergeben kann.
Das Design soll modern sein, aber auch Seriösität vermitteln. Durch meine über 10 jährige Tätigkeit als Sachverständiger für Immobilienbewertung hebe ich mich vom know how deutlich von den meisten Maklern ab.
Die Bürodaten (Anschrift usw.) können von meinem Auftritt des Sachverständigenbüros entnommen werden: www.taxfeld.net

```html
<!DOCTYPE html>
<html lang="de">
<head>
<meta charset="utf-8">
<title>Hauslumora – Briefpapier</title>
<link href="https://fonts.googleapis.com/css2?family=Arimo:wght@400;700&display=swap" rel="stylesheet">
<style>
  :root {
    --brand-blue: #0a4a7e;
    --ink: #1a1a1a;
    --muted: #6b6b6b;
    --rule: #9a9a9a;
    --paper: #ffffff;
    --backdrop: #f2f2f2;
  }
  * { margin: 0; padding: 0; box-sizing: border-box; }
  html, body { width: 1200px; height: 1200px; overflow: hidden; }
  body { background: var(--backdrop); font-family: "Arimo", Arial, sans-serif; color: var(--ink); }
  .letterhead {
    position: absolute; left: 200px; top: 31px; width: 804px; height: 1137px;
    background: var(--paper);
  }
  .side-band { position: absolute; left: 0; top: 0; width: 76px; height: 1039px; background: var(--brand-blue); }
  .brand-name {
    position: absolute; right: 42px; top: 100px;
    font-size: 25px; font-weight: 700; letter-spacing: 1px; color: var(--brand-blue);
  }
  .sender-line { position: absolute; left: 116px; top: 153px; font-size: 10.5px; }
  .recipient { position: absolute; left: 116px; top: 172px; font-size: 10.5px; line-height: 12px; }
  .letter-body { position: absolute; left: 116px; top: 358px; width: 580px; font-size: 11.6px; line-height: 17px; }
  .letter-body p { margin-bottom: 17px; }
  .closing { position: absolute; left: 116px; top: 816px; font-size: 11.6px; }
  .signatory { position: absolute; left: 114px; top: 934px; font-size: 13.5px; line-height: 15px; }
  .brand-mark {
    position: absolute; left: 358px; top: 945px;
    font-size: 16px; font-weight: 700; letter-spacing: 1px; color: var(--brand-blue);
  }
  .footer-rule { position: absolute; left: 76px; top: 1038px; width: 690px; height: 1px; background: var(--rule); }
  .footer { position: absolute; left: 0; top: 1049px; width: 800px; text-align: center; font-size: 10.5px; color: var(--muted); line-height: 24px; }
</style>
</head>
<body>
  <main class="letterhead">
    <div class="side-band"></div>
    <div class="brand-name">HAUSLUMORA</div>

    <div class="sender-line">Name Name - Strasse 1 - Strasse 2</div>
    <address class="recipient" style="font-style:normal">Max Mustermann<br>Straße<br>Ort</address>

    <section class="letter-body">
      <p>Sehr geehrter Herr,</p>
      <p>Esse ut ex. Sed esse mollit quis laboris in pariatur, anim ut aliquip ullamco voluptate. Ex consectetur culpa<br>in eu, proident aliqua mollit sint reprehenderit?</p>
      <p>Incididunt ut in dolore reprehenderit aliqua ad, mollit anim fugiat ea. Enim consequat ad, ipsum ad sint<br>culpa amet consectetur, sed cupidatat. Sit commodo ut. Non, nisi excepteur, fugiat voluptate ullamco eu<br>labore: Pariatur sint laboris. Ipsum ea culpa qui nisi id exercitation, voluptate sit qui esse. Nisi, sunt ipsum<br>occaecat commodo ut, magna veniam sed sit. Nisi officia minim reprehenderit dolore exercitation in fugiat,<br>pariatur do reprehenderit dolore? Dolore, nostrud dolor velit.</p>
      <p>Aute aliqua, sed nostrud ut in ex nulla id ut non mollit aute voluptate. Occaecat anim ea nostrud et dolor<br>est fugiat tempor excepteur. Amet, esse culpa commodo proident ut commodo do aute.<br>Qui sed adipisicing voluptate est. Fugiat sint veniam in duis non deserunt sint commodo: Occaecat dolore<br>magna ea mollit, enim dolor exercitation dolore sunt magna aute lorem ea ad exercitation?</p>
      <p>Consectetur id ea proident. Dolore sunt velit et reprehenderit aliqua eiusmod. Exercitation eu laboris ex<br>occaecat deserunt dolore et excepteur sint in dolore nostrud laboris dolore culpa quis cupidatat. Ea cillum<br>et. In, consectetur amet.</p>
      <p>In elit ullamco culpa, enim reprehenderit est dolore magna, ad lorem. Ipsum ea, minim mollit sit minim.<br>Sed voluptate velit dolor in magna non aliqua cillum in officia in excepteur.Officia veniam ut, pariatur ad<br>veniam reprehenderit ex sint consequat magna. Amet sunt, duis velit do qui culpa, adipisicing sint mollit<br>officia in culpa aliqua. Lorem, aliqua non labore est enim. Ad officia commodo do eu consequat. Sunt in,<br>eu cupidatat, qui aute proident, adipisicing fugiat dolore velit ut in sint eiusmod commodo laboris do.</p>
    </section>

    <div class="closing">Mit freundlichen Grüßen</div>
    <div class="signatory">Name Name<br>Geschäftsführerin</div>
    <div class="brand-mark">HAUSLUMORA</div>

    <div class="footer-rule"></div>
    <footer class="footer">
      Name Name • Strasse 1 • Strasse 2<br>
      Tel: +43 (0) 123456 • Fax: +43 (0) 123456 • E-mail: kontakt@velmarin.at • Web: www.velmarin.at<br>
      Bankverbindung: xxxxxxxxxx • IBAN: xxxxxxxxxxxxxx • BIC: xxxxxxxxxxxxxxxxxx
    </footer>
  </main>
</body>
</html>
```